Business card: floral shop

I own a flower shop that specializes in Japanese flower settings and weddings. I am looking for a design that has to be colorful, but elegantly simple (unadorned), while implying class, love, and commitment.

My flower shop is also all about outstanding customer service, if this helps at all.

Industry/Entity Type

Floral

Contact Information for Business Card

Company Name: Brightwater Bloom Studio
Name: Marisol Keene
Address: 41 Larkspur Rd, Wexley, MA 01836
Email: petalcrestmail@fernovo.com

Logo Text

Brightwater Bloom Studio

Requirements
Must have
• Flowers, color, company information.

Offer:

"Refer a friend and receive $25 gift certificate at the time of the order"
Should not have
• Black borders

```html
<!DOCTYPE html>
<html lang="en">
<head>
<meta charset="utf-8">
<title>Brightwater Bloom Studio – Business Card</title>
<link rel="stylesheet" href="https://fonts.googleapis.com/css2?family=Pinyon+Script&family=Cinzel:wght@400&family=Open+Sans:wght@400&display=swap">
<style>
  :root {
    --paper-light: #f4f7ef;
    --paper-edge: #dde6d2;
    --brand-rose: #c98f96;
    --label-rose: #d07a86;
    --ink: #111111;
    --tulip-pink: #e0566f;
    --tulip-deep: #c63a57;
    --stem-green: #8cc45a;
  }
  html, body {
    margin: 0;
    padding: 0;
    overflow: hidden;
    background: #ffffff;
  }
  .card {
    position: relative;
    width: 1200px;
    height: 720px;
    overflow: hidden;
    background: radial-gradient(ellipse 70% 75% at 45% 45%, var(--paper-light) 0%, #eef3e7 50%, var(--paper-edge) 100%);
  }
  .studio-name {
    position: absolute;
    top: 78px;
    left: 0;
    width: 1200px;
    margin: 0;
    text-align: center;
    font-family: "Pinyon Script", cursive;
    font-weight: 400;
    font-size: 84px;
    line-height: 1.2;
    color: var(--brand-rose);
  }
  .florist-name {
    position: absolute;
    left: 60px;
    top: 350px;
    margin: 0;
    font-family: "Cinzel", serif;
    font-weight: 400;
    font-size: 62px;
    letter-spacing: 2px;
    line-height: 1;
    color: var(--ink);
  }
  .contact {
    position: absolute;
    left: 64px;
    top: 570px;
    margin: 0;
    font-family: "Open Sans", sans-serif;
    font-size: 28px;
    line-height: 48px;
  }
  .contact-row {
    display: flex;
    margin: 0;
  }
  .contact-label {
    color: var(--label-rose);
    font-style: italic;
  }
  .contact-label.email { width: 146px; }
  .contact-label.address { width: 132px; }
  .contact-value {
    color: var(--ink);
    margin: 0;
  }
  .bouquet {
    position: absolute;
    right: 0;
    bottom: 0;
    width: 470px;
    height: 520px;
  }
</style>
</head>
<body>
  <main class="card">
    <h1 class="studio-name">Brightwater Bloom Studio</h1>

    <h2 class="florist-name">Marisol Keene</h2>

    <dl class="contact">
      <div class="contact-row">
        <dt class="contact-label email">Email:</dt>
        <dd class="contact-value">petalcrestmail@fernovo.com</dd>
      </div>
      <div class="contact-row">
        <dt class="contact-label address">Address:</dt>
        <dd class="contact-value">41 Larkspur Rd, Wexley, MA 01836</dd>
      </div>
    </dl>

    <svg class="bouquet" viewBox="0 0 470 520" role="img" aria-label="Photograph of a bouquet of pink tulips with green stems and leaves">
      <defs>
        <linearGradient id="bouquet-tone" x1="0" y1="0" x2="1" y2="1">
          <stop offset="0" stop-color="var(--tulip-pink)"/>
          <stop offset="0.6" stop-color="var(--tulip-deep)"/>
          <stop offset="1" stop-color="var(--stem-green)"/>
        </linearGradient>
      </defs>
      <path d="M60 160 C 80 90, 150 50, 230 40 C 300 20, 360 10, 400 30 C 440 60, 450 130, 470 200 L 470 520 L 150 520 C 110 480, 30 420, 20 350 C 5 280, 30 210, 60 160 Z" fill="url(#bouquet-tone)" opacity="0.85"/>
    </svg>
  </main>
</body>
</html>
```